Bright Meadow Cabins Needs A Flyer

We need a flyer for our newest product "The Sunlit Garden Workpod Deluxe"

Here is some copy for the flyer:

1. More and more people everyday are working from home and finding it difficult to disconnect from home activities in order to focus on their work. They are also finding it very expensive to add on to their existing house for a quiet place. Our archatectually stunning, Sunlit Garden Workpod Deluxe is the answer. The office studio measures 16' wide and 10' deep. 160 Square feet of space.

Perfect for dozens of purposes. Home office, design studio, artist studio, home school office, reading room, craft studio, drafting room.

Features include:

- Steel Framing. 40-60% lighter then wood, higher strength to weight ratio, resistant to mold and fire and steel is the most recycled material on earth!
- Spray foam insulation. Cool in the summer and warm in the winter.
- HVAC Mini Split with wireless remote control and thermostat.
- 100% Off grid with enough solar and battery storage to run your entire office. No need to pay for an expensive electric installation.
- Flush fitting floor outlets to reduce wires.
- TV mount (Optional with pre-wired electric, HDMI, digital audio & Cat 6)
- Windows are tempered glass custom made by Vorn Glazing.
- Solar qualifies for a 26% tax credit. This is not a write-off rather it is a direct reduction on your tax obligation.
- Thousands of dollars less than adding onto your home.
- Custom color, siding, features available.

This beautiful back yard office is delivered 100% assembled and ready to enjoy on the day of delivery.

We ship nationwide from our factory in South Carolina. Give us a call anytime to speak to a designer and start your dream office today!

555-318-4720
info@BrightMeadowCabins.example

```html
<!DOCTYPE html>
<html lang="en">
<head>
<meta charset="utf-8">
<title>Bright Meadow Cabins – The Sunlit Garden Workpod Deluxe</title>
<link href="https://fonts.googleapis.com/css2?family=Lobster&family=Hind:wght@400;500;600;700&display=swap" rel="stylesheet">
<style>
  :root{
    --orange:#f7a823;
    --orange-deep:#f09a12;
    --green:#5a9e3e;
    --green-dark:#3f8a2b;
    --charcoal:#333333;
    --ink:#2b2622;
    --white:#ffffff;
    --body:#333333;
  }
  *{box-sizing:border-box;margin:0;padding:0}
  html,body{width:902px;height:1200px;overflow:hidden;background:var(--white)}
  body{font-family:"Hind",Arial,sans-serif;color:var(--body)}
  .flyer{position:relative;width:902px;height:1200px;overflow:hidden;background:var(--white)}
  .backdrop{position:absolute;inset:0}
  .abs{position:absolute;z-index:1}

  .brand{left:52px;top:118px;display:flex;align-items:center;gap:12px}
  .brand-mark{width:24px;height:24px;background:var(--orange);flex:none}
  .brand-name{font-family:"Hind",Arial,sans-serif;font-weight:700;font-size:30px;color:var(--green);line-height:1.05}

  .title{left:62px;top:236px;color:var(--ink);font-family:"Lobster",cursive;font-weight:400}
  .title-main{font-size:76px;line-height:1}
  .title-sub{font-size:40px;line-height:1.1;margin-top:4px}

  .intro{left:441px;top:410px;width:418px;color:var(--white);font-size:14.5px;font-weight:600;line-height:1.32;text-align:justify}
  .intro-size{margin-top:12px;font-style:italic;font-weight:700;font-size:15px;line-height:1.3;text-transform:uppercase}

  .purposes{left:65px;top:606px;width:295px;text-align:center}
  .purposes-head{font-family:"Lobster",cursive;font-weight:400;font-size:29px;line-height:1.2;color:var(--ink)}
  .purposes-list{list-style:none;margin-top:12px;font-weight:600;font-size:19.5px;line-height:25.5px;color:var(--ink)}

  .delivery{left:65px;top:918px;width:295px;text-align:center;color:var(--white);font-weight:600;font-size:15.5px;line-height:1.3}
  .delivery-strong{display:block;color:var(--orange);font-size:22px;font-weight:700;line-height:1.25}

  .features{left:420px;top:762px;width:420px}
  .features-head{color:var(--green);font-weight:700;font-size:18px;letter-spacing:.2px}
  .features-list{list-style:none;margin-top:8px}
  .feature{display:flex;gap:12px;font-size:12.5px;line-height:16px;margin-bottom:4.5px;color:var(--body);font-style:italic}
  .feature-dot{flex:none;width:9px;height:9px;margin-top:3px;margin-left:2px;border-radius:50%;background:var(--green)}

  .ship{left:60px;top:1054px;width:336px;text-align:center;color:var(--white);font-weight:600;font-size:12.5px;line-height:1.35}
  .phone{left:62px;top:1132px;display:flex;align-items:center;gap:14px;color:var(--white);font-weight:700;font-size:34px;line-height:1}
  .divider{left:414px;top:1130px;width:1px;height:50px;background:rgba(255,255,255,.5)}
  .email{left:440px;top:1146px;display:flex;align-items:center;gap:12px;color:var(--white);font-weight:600;font-size:13.5px}
  .email-label{font-size:12.5px;margin-right:4px}
  .icon-badge{width:26px;height:26px;border-radius:50%;background:var(--orange);display:flex;align-items:center;justify-content:center;flex:none}
</style>
</head>
<body>
<div class="flyer">

  <svg class="backdrop" width="902" height="1200" viewBox="0 0 902 1200" aria-hidden="true">
    <defs>
      <linearGradient id="orangeBand" x1="0" y1="0" x2="0" y2="1">
        <stop offset="0" stop-color="#f49d14"/>
        <stop offset="1" stop-color="#fbbf3c"/>
      </linearGradient>
      <linearGradient id="orangePanel" x1="0" y1="0" x2="0" y2="1">
        <stop offset="0" stop-color="#fbbd3a"/>
        <stop offset="1" stop-color="#f39c15"/>
      </linearGradient>
      <linearGradient id="softGrey" x1="1" y1="0" x2="0" y2="0">
        <stop offset="0" stop-color="#d9d9d9"/>
        <stop offset="1" stop-color="#ffffff"/>
      </linearGradient>
    </defs>
    <path d="M0,200 Q230,175 400,250 Q520,300 902,300 L902,440 Q600,395 0,445 Z" fill="url(#orangeBand)"/>
    <path d="M0,445 Q600,395 902,428 L902,622 Q700,596 520,620 Q450,630 380,630 L0,630 Z" fill="var(--green)"/>
    <path d="M380,630 Q450,630 520,620 Q700,596 902,622 L902,1130 L380,1130 Z" fill="url(#softGrey)" opacity=".8"/>
    <path d="M0,1030 L360,1030 Q470,1030 560,1080 Q680,1140 902,1122 L902,1200 L0,1200 Z" fill="var(--green)"/>
    <rect x="65" y="589" width="295" height="330" fill="url(#orangePanel)"/>
    <polygon points="65,905 212,880 360,905 360,1040 65,1040" fill="var(--charcoal)"/>
  </svg>

  <svg class="abs" style="left:0;top:0;z-index:0" width="902" height="320" viewBox="0 0 902 320" role="img" aria-label="Photo of the garden workpod with solar panels on its roof, set in a landscaped back yard">
    <defs>
      <linearGradient id="heroScene" x1="0" y1="0" x2="0" y2="1">
        <stop offset="0" stop-color="#b9d3e6"/>
        <stop offset=".45" stop-color="#5f7d4f"/>
        <stop offset=".7" stop-color="#4b5048"/>
        <stop offset="1" stop-color="#6b9a3f"/>
      </linearGradient>
    </defs>
    <path d="M318,0 L902,0 L902,300 Q600,305 450,255 Q340,215 318,0 Z" fill="url(#heroScene)" stroke="#ffffff" stroke-width="6"/>
  </svg>

  <div class="brand abs">
    <span class="brand-mark"></span>
    <span class="brand-name">Bright Meadow<br>Cabins</span>
  </div>

  <h1 class="title abs">
    <div class="title-main">The Sunlit</div>
    <div class="title-sub">Garden Workpod Deluxe</div>
  </h1>

  <svg class="abs" style="left:44px;top:388px" width="362" height="200" viewBox="0 0 362 200" role="img" aria-label="Render of the workpod front with full-height glass doors and windows">
    <defs>
      <linearGradient id="podRender" x1="0" y1="0" x2="0" y2="1">
        <stop offset="0" stop-color="#3a3a3a"/>
        <stop offset=".5" stop-color="#8d8a84"/>
        <stop offset="1" stop-color="#3f3f3f"/>
      </linearGradient>
    </defs>
    <rect x="0" y="0" width="362" height="200" fill="url(#podRender)"/>
  </svg>

  <div class="intro abs">
    <p>More and more people everyday are working from home and finding it difficult to disconnect from home activities in order to focus on their work. They are also finding it very expensive to add on to their existing house for a quiet place. Our archatectually stunning, Sunlit Garden Workpod Deluxe is the answer.</p>
    <p class="intro-size">The office studio measures 16' wide and 10' deep.<br>160 square feet of space.</p>
  </div>

  <div class="purposes abs">
    <h2 class="purposes-head">Perfect for<br>dozens of purposes</h2>
    <ul class="purposes-list">
      <li>Home office</li>
      <li>Design studio</li>
      <li>Artist studio</li>
      <li>Home school office</li>
      <li>Reading room</li>
      <li>Craft studio</li>
      <li>Drafting room</li>
    </ul>
  </div>

  <p class="delivery abs">This beautiful back yard office<br>is delivered<span class="delivery-strong">100% assembled</span>and ready to enjoy on the day<br>of delivery.</p>

  <svg class="abs" style="left:392px;top:628px" width="200" height="116" viewBox="0 0 200 116" role="img" aria-label="Render of the steel frame structure of the workpod">
    <rect width="200" height="116" fill="#e4e4e4"/>
  </svg>
  <svg class="abs" style="left:612px;top:635px" width="246" height="112" viewBox="0 0 246 112" role="img" aria-label="Render of the finished workpod exterior">
    <rect width="246" height="112" fill="#6a6763"/>
  </svg>

  <div class="features abs">
    <h2 class="features-head">FEATURES INCLUDE:</h2>
    <ul class="features-list">
      <li class="feature"><span class="feature-dot"></span><span>Steel Framing. 40-60% lighter then wood, higher strength to weight ratio, resistant to mold and fire and steel is the most recycled material on earth!</span></li>
      <li class="feature"><span class="feature-dot"></span><span>Spray foam insulation. Cool in the summer and warm in the winter.</span></li>
      <li class="feature"><span class="feature-dot"></span><span>HVAC Mini Split with wireless remote control and thermostat.</span></li>
      <li class="feature"><span class="feature-dot"></span><span>100% Off grid with enough solar and battery storage to run your entire office. No need to pay for an expensive electric installation.</span></li>
      <li class="feature"><span class="feature-dot"></span><span>Flush fitting floor outlets to reduce wires.</span></li>
      <li class="feature"><span class="feature-dot"></span><span>TV mount (Optional with pre-wired electric, HDMI, digital audio &amp; Cat 6)</span></li>
      <li class="feature"><span class="feature-dot"></span><span>Windows are tempered glass custom made by Vorn Glazing.</span></li>
      <li class="feature"><span class="feature-dot"></span><span>Solar qualifies for a 26% tax credit. This is not a write-off rather it is a direct reduction on your tax obligation.</span></li>
      <li class="feature"><span class="feature-dot"></span><span>Thousands of dollars less than adding onto your home.</span></li>
      <li class="feature"><span class="feature-dot"></span><span>Custom color, siding, features available.</span></li>
    </ul>
  </div>

  <p class="ship abs">We ship nationwide from our factory<br>in South Carolina.<br>Give us a call anytime to speak to a<br>designer and start your dream office today!</p>

  <div class="phone abs">
    <span class="icon-badge" style="width:30px;height:30px">
      <svg width="16" height="16" viewBox="0 0 24 24" aria-hidden="true"><path d="M6.6 10.8a15.5 15.5 0 0 0 6.6 6.6l2.2-2.2a1 1 0 0 1 1-.25 11.4 11.4 0 0 0 3.6.57 1 1 0 0 1 1 1V20a1 1 0 0 1-1 1A17 17 0 0 1 3 4a1 1 0 0 1 1-1h3.5a1 1 0 0 1 1 1c0 1.25.2 2.45.57 3.57a1 1 0 0 1-.25 1z" fill="#ffffff"/></svg>
    </span>
    <span>555-318-4720</span>
  </div>

  <div class="divider abs"></div>

  <div class="email abs">
    <span class="email-label">Email us :</span>
    <span class="icon-badge">
      <svg width="14" height="14" viewBox="0 0 24 24" aria-hidden="true"><rect x="2" y="5" width="20" height="14" rx="2" fill="#ffffff"/><path d="M3 6l9 7 9-7" stroke="#f7a823" stroke-width="2" fill="none"/></svg>
    </span>
    <span>info@BrightMeadowCabins.example</span>
  </div>

</div>
</body>
</html>
```